Exciting new branding of Recruitment Company based on it's new website

We have an exciting new website we are about to launch and would like to have letterhead, business cards, email signature options, email banner, linkedin and facebook cover images all refreshed to match the website. I have attached the existing logo. The website is at http://brightcrewhire.samplehost.com/ and we are particularly interested in the grey with orange writing at the base of the first page where it says Register Now

Target Market(s)

Recruitment

Contact Information for Business Card

Dana Holt
Account Executive
T: 1300 582 317
M: 0412 637 845
E: dana@brightcrewhire.com.au
W: brightcrewhire.com.au
A: Suite 3, 42 Tamsin Court, Deakin ACT 2600
ABN: 52 418 736 904

Font styles to use
Serif
Sans Serif

Requirements
Must have
• The grey colour from the website

```html
<!DOCTYPE html>
<html lang="en">
<head>
<meta charset="utf-8">
<title>Bright Crew Hire – Stationery Suite</title>
<link href="https://fonts.googleapis.com/css2?family=Roboto:wght@400;500;700&display=swap" rel="stylesheet">
<style>
  :root{
    --orange:#f5ad4c;
    --board:#e3e3e3;
    --label:#a9a9a9;
    --ink:#222222;
    --white:#ffffff;
    --photo-dark:#6e6e6e;
    --photo-light:#d6d6d6;
  }
  *{box-sizing:border-box;margin:0;padding:0}
  html,body{width:968px;height:1200px;overflow:hidden}
  body{background:var(--board);font-family:'Roboto',Arial,sans-serif;color:var(--ink);position:relative}
  .section-label{position:absolute;font-size:16px;color:var(--label);font-weight:400;letter-spacing:.2px}
  .piece{position:absolute;background:var(--white);overflow:hidden;box-shadow:0 1px 3px rgba(0,0,0,.25)}
  .photo{position:absolute;left:0;top:0;width:100%;height:100%;
    background:linear-gradient(135deg,var(--photo-light) 0%,#9a9a9a 45%,var(--photo-dark) 100%)}
  .band{position:absolute;left:0;top:0;width:100%;background:var(--orange)}
  .contacts{position:absolute;list-style:none}
  .contacts li{display:flex;align-items:center;white-space:nowrap}
  .contacts svg{fill:var(--orange);flex:none}
  .contacts .abn{padding-left:var(--indent)}
  .lockup{position:absolute;display:flex;align-items:center;font-weight:700;line-height:.95}
  .lockup .dot{border-radius:50%;flex:none}
  .social{position:absolute;display:flex}
  .social span{border-radius:50%;background:var(--orange)}

  /* Letterhead */
  .letterhead{left:503px;top:84px;width:394px;height:557px}
  .letterhead .head-band{position:absolute;left:192px;top:54px;width:202px;height:22px;background:var(--orange);
    clip-path:polygon(0 0,100% 0,100% 100%,22px 100%)}
  .letter-body{position:absolute;left:54px;top:118px;width:292px;font-size:5px;line-height:7.2px;font-weight:500}
  .letter-body p{margin-bottom:7px}
  .letter-body .greeting{margin-bottom:14px}
  .letter-body .signoff{margin-top:22px}
  .letterhead .footer{position:absolute;left:0;bottom:0;width:100%;height:30px;background:var(--orange);
    color:var(--white);font-size:6.5px}
  .letterhead .footer span{position:absolute;top:11px;display:flex;align-items:center;gap:3px}
  .letterhead .footer svg{fill:var(--white)}

  /* Email signature */
  .signature{left:60px;top:278px;width:417px;height:140px}
  .signature .name{position:absolute;left:133px;top:8px;color:var(--white);font-size:24px;font-weight:500}
  .signature .role{position:absolute;left:133px;top:37px;color:var(--white);font-size:8.5px;letter-spacing:2.6px}
</style>
</head>
<body>

<svg width="0" height="0" style="position:absolute" aria-hidden="true">
  <symbol id="i-pin" viewBox="0 0 10 10"><path d="M5 0a3.6 3.6 0 0 0-3.6 3.6C1.4 6.3 5 10 5 10s3.6-3.7 3.6-6.4A3.6 3.6 0 0 0 5 0zm0 5.1a1.5 1.5 0 1 1 0-3 1.5 1.5 0 0 1 0 3z"/></symbol>
  <symbol id="i-phone" viewBox="0 0 10 10"><path d="M2 .6l1.6-.2 1 2.4-1.1.9a6 6 0 0 0 2.8 2.8l.9-1.1 2.4 1-.2 1.6C9.2 9.3 8.5 9.7 7.8 9.6 4.1 9 1 5.9.4 2.2.3 1.5.7.8 2 .6z"/></symbol>
  <symbol id="i-mail" viewBox="0 0 10 10"><path d="M0 2h10v6H0zM.8 2.6L5 5.6l4.2-3z" fill-rule="evenodd"/></symbol>
  <symbol id="i-pointer" viewBox="0 0 10 10"><path d="M2 0l6.5 6.2-2.9.3 1.7 3-1.2.5-1.6-3L2.3 9z"/></symbol>
</svg>

<!-- Letterhead -->
<div class="section-label" style="left:503px;top:63px">Lletterhead</div>
<div class="piece letterhead">
  <div class="lockup" style="left:53px;top:58px;color:var(--orange);font-size:7px;gap:4px">
    <span class="dot" style="width:14px;height:14px;border:2px solid var(--orange)"></span>
    <span>bright crew<br>hire</span>
  </div>
  <div class="head-band"></div>
  <div class="letter-body">
    <p class="greeting">Dear Hiring Manager,</p>
    <p>Thank you for choosing Bright Crew Hire as your recruitment partner. We take pride in matching capable people with teams that value them, and we work closely with every client to understand the roles they need to fill. Our consultants bring deep local knowledge, a wide network of candidates and a clear, honest process from the first call to the final placement.</p>
    <p>Over the coming weeks we will review your hiring needs, prepare a short list of suitable candidates and arrange interviews at times that suit your team. Each candidate is screened for skills, experience and fit before we put their name forward. We also check references and confirm availability so that you can make decisions with confidence. Should your needs change at any stage, simply let us know and we will adjust our search. Our aim is to save you time, reduce risk and help you build a stronger, more settled workforce for the years ahead.</p>
    <p>Our team is available Monday to Friday and can also meet with you on site to discuss larger projects, seasonal demand or ongoing staffing arrangements across the region.</p>
    <p>If you have any questions about this letter or our terms of engagement, please contact me directly by phone or email and I will be glad to help as soon as possible.</p>
    <p>We look forward to working with you and your team.</p>
    <p class="signoff">Best Regards.</p>
  </div>
  <div class="social" style="left:28px;top:515px;gap:7px" aria-label="Social media links">
    <span style="width:8px;height:8px"></span><span style="width:8px;height:8px"></span><span style="width:8px;height:8px"></span><span style="width:8px;height:8px"></span>
  </div>
  <div class="footer">
    <span style="left:27px"><svg width="6" height="6"><use href="#i-phone"/></svg>1300 582 317</span>
    <span style="left:140px"><svg width="7" height="7"><use href="#i-mail"/></svg>dana@brightcrewhire.com.au</span>
    <span style="left:289px"><svg width="6" height="6"><use href="#i-pointer"/></svg>brightcrewhire.com.au</span>
  </div>
</div>

<!-- Email signature -->
<div class="section-label" style="left:60px;top:255px">Email signature</div>
<div class="piece signature">
  <div class="photo" role="img" aria-label="Black-and-white overhead photo of a shared desk with laptops, notebooks and coffee cups"
       style="clip-path:polygon(0 0,61px 0,127px 68px,81px 140px,0 140px)"></div>
  <div class="band" style="height:68px;clip-path:polygon(61px 0,100% 0,100% 100%,127px 100%)"></div>
  <div class="name">Dana Holt</div>
  <div class="role">Account Executive</div>
  <ul class="contacts" style="left:134px;top:80px;font-size:7.6px;line-height:11.4px;--indent:14px">
    <li><svg width="8" height="8" style="margin-right:6px"><use href="#i-pin"/></svg>Suite 3, 42 Tamsin Court, Deakin ACT 2600</li>
    <li><svg width="8" height="8" style="margin-right:6px"><use href="#i-phone"/></svg>1300 582 317 / 0412 637 845</li>
    <li><svg width="8" height="8" style="margin-right:6px"><use href="#i-mail"/></svg>dana@brightcrewhire.com.au</li>
    <li><svg width="8" height="8" style="margin-right:6px"><use href="#i-pointer"/></svg>brightcrewhire.com.au</li>
    <li class="abn" style="font-size:6px">ABN: 52 418 736 904</li>
  </ul>
  <div class="social" style="left:361px;top:74px;gap:4px" aria-label="Social media links">
    <span style="width:8px;height:8px"></span><span style="width:8px;height:8px"></span><span style="width:8px;height:8px"></span><span style="width:8px;height:8px"></span>
  </div>
  <div class="lockup" style="left:345px;top:98px;color:var(--orange);font-size:8px;gap:5px">
    <span class="dot" style="width:24px;height:24px;border:2.5px solid var(--orange)"></span>
    <span>bright crew<br>hire</span>
  </div>
</div>

<!-- Facebook banner -->
<div class="section-label" style="left:60px;top:442px">Facebook banner</div>
<div class="piece" style="left:60px;top:462px;width:406px;height:178px">
  <div class="photo" role="img" aria-label="Black-and-white overhead photo of a shared desk with laptops, notebooks and coffee cups"
       style="clip-path:polygon(0 0,69px 0,156px 85px,94px 178px,0 178px)"></div>
  <div class="band" style="height:85px;clip-path:polygon(69px 0,100% 0,100% 100%,156px 100%)"></div>
  <div class="lockup" style="left:203px;top:22px;color:var(--white);font-size:16px;gap:9px">
    <span class="dot" style="width:44px;height:44px;border:4px solid var(--white)"></span>
    <span>bright crew<br>hire</span>
  </div>
  <ul class="contacts" style="left:164px;top:95px;font-size:9px;line-height:13.7px;--indent:16px">
    <li><svg width="9" height="9" style="margin-right:7px"><use href="#i-pin"/></svg>Suite 3, 42 Tamsin Court, Deakin ACT 2600</li>
    <li><svg width="9" height="9" style="margin-right:7px"><use href="#i-phone"/></svg>1300 582 317 / 0412 637 845</li>
    <li><svg width="9" height="9" style="margin-right:7px"><use href="#i-mail"/></svg>dana@brightcrewhire.com.au</li>
    <li><svg width="9" height="9" style="margin-right:7px"><use href="#i-pointer"/></svg>brightcrewhire.com.au</li>
    <li class="abn" style="font-size:7px">ABN: 52 418 736 904</li>
  </ul>
</div>

<!-- LinkedIn banner -->
<div class="section-label" style="left:60px;top:671px">Linkedin banner</div>
<div class="piece" style="left:60px;top:691px;width:548px;height:165px">
  <div class="photo" role="img" aria-label="Black-and-white overhead photo of a shared desk with laptops, notebooks and coffee cups"
       style="clip-path:polygon(0 0,69px 0,162px 79px,90px 165px,0 165px)"></div>
  <div class="band" style="height:79px;clip-path:polygon(69px 0,100% 0,100% 100%,162px 100%)"></div>
  <div class="lockup" style="left:276px;top:19px;color:var(--white);font-size:13px;gap:8px">
    <span class="dot" style="width:38px;height:38px;border:3.5px solid var(--white)"></span>
    <span>bright crew<br>hire</span>
  </div>
  <ul class="contacts" style="left:166px;top:89px;font-size:8.5px;line-height:12.9px;--indent:15px">
    <li><svg width="8" height="8" style="margin-right:7px"><use href="#i-pin"/></svg>Suite 3, 42 Tamsin Court, Deakin ACT 2600</li>
    <li><svg width="8" height="8" style="margin-right:7px"><use href="#i-phone"/></svg>1300 582 317 / 0412 637 845</li>
    <li><svg width="8" height="8" style="margin-right:7px"><use href="#i-mail"/></svg>dana@brightcrewhire.com.au</li>
    <li><svg width="8" height="8" style="margin-right:7px"><use href="#i-pointer"/></svg>brightcrewhire.com.au</li>
    <li class="abn" style="font-size:6.5px">ABN: 52 418 736 904</li>
  </ul>
</div>

<!-- Business card -->
<div class="section-label" style="left:60px;top:906px">Bussiness card</div>
<div class="piece" style="left:60px;top:926px;width:339px;height:194px">
  <span style="position:absolute;left:265px;top:26px;width:34px;height:34px;border-radius:50%;border:3px solid var(--orange)"></span>
  <div style="position:absolute;left:22px;top:56px;color:var(--orange);font-size:25px;font-weight:500">Dana Holt</div>
  <div style="position:absolute;left:22px;top:81px;font-size:10px;letter-spacing:1.5px;font-weight:500">Account Executive</div>
  <div style="position:absolute;left:22px;top:98px;width:162px;height:1px;background:var(--orange)"></div>
  <ul class="contacts" style="left:23px;top:106px;font-size:10px;line-height:15px;--indent:17px">
    <li><svg width="9" height="9" style="margin-right:8px"><use href="#i-pin"/></svg>Suite 3, 42 Tamsin Court, Deakin ACT 2600</li>
    <li><svg width="9" height="9" style="margin-right:8px"><use href="#i-phone"/></svg>1300 582 317 / 0412 637 845</li>
    <li><svg width="9" height="9" style="margin-right:8px"><use href="#i-mail"/></svg>dana@brightcrewhire.com.au</li>
    <li><svg width="9" height="9" style="margin-right:8px"><use href="#i-pointer"/></svg>brightcrewhire.com.au</li>
    <li class="abn" style="font-size:8px;font-weight:700;margin-top:2px">ABN: 52 418 736 904</li>
  </ul>
</div>
<div class="piece" style="left:436px;top:924px;width:345px;height:196px;background:var(--orange)">
  <div class="lockup" style="left:56px;top:38px;color:var(--white);font-size:28px;gap:16px">
    <span class="dot" style="width:100px;height:100px;border:8px solid var(--white)"></span>
    <span>bright crew<br>hire</span>
  </div>
</div>

</body>
</html>
```